Elegant and Professional Business card design needed

The patron journey mentor is a company which provides consulting services to businesses to assist them in improving the customer experience for their customers.

I need a business card design which tells people I'm there to help them.

Target Market(s)

Small to medium business owners

Industry/Entity Type

Business

Contact Information for Business Card

Martin Glenholme
The Patron Journey Mentor
Web: http://www.ThePatronJourneyMentor.example
Email: martin@ThePatronJourneyMentor.example
Phone: +61 400 582316

Logo styles of interest
Abstract Logo
Requirements
Must have
• Some sort of image / graphic representing the customer is important and should be at the heart of a business.

```html
<!DOCTYPE html>
<html lang="en">
<head>
<meta charset="utf-8">
<title>The Patron Journey Mentor – Business Card</title>
<link rel="stylesheet" href="https://fonts.googleapis.com/css2?family=Questrial&family=Arimo:wght@700&family=Tinos&display=swap">
<style>
  :root {
    --stage: #1c2a3d;
    --brand-blue: #2e6189;
    --brand-blue-dark: #1f5a80;
    --figure-blue: #244f72;
    --paper: #ffffff;
    --paper-shade: #f1f1f3;
  }
  html, body {
    margin: 0;
    padding: 0;
    width: 1200px;
    height: 970px;
    overflow: hidden;
    background: var(--stage);
  }
  .business-card {
    position: absolute;
    left: 98px;
    top: 202px;
    width: 1005px;
    height: 568px;
    background: linear-gradient(135deg, var(--paper) 55%, var(--paper-shade) 100%);
    overflow: hidden;
    font-family: "Questrial", "Century Gothic", sans-serif;
  }
  .panel-left {
    position: absolute;
    left: 0; top: 0;
    width: 517px; height: 523px;
    background: var(--brand-blue);
  }
  .footer-strip-right {
    position: absolute;
    left: 517px; top: 523px;
    width: 488px; height: 45px;
    background: var(--brand-blue);
  }
  .title-band {
    position: absolute;
    left: 272px; top: 81px;
    width: 245px; height: 99px;
    background: var(--paper);
  }
  .name-band {
    position: absolute;
    left: 517px; top: 180px;
    width: 213px; height: 98px;
    background: var(--brand-blue);
  }
  .pointing-hand-left {
    position: absolute;
    left: 37px; top: 66px;
    width: 245px; height: 97px;
    background: var(--paper);
    border-radius: 40px 6px 6px 40px;
  }
  .pointing-hand-right {
    position: absolute;
    left: 722px; top: 163px;
    width: 265px; height: 100px;
    background: var(--brand-blue);
    border-radius: 6px 40px 40px 6px;
  }
  .consultant-figure {
    position: absolute;
    left: 72px; top: 166px;
    width: 245px; height: 355px;
    background: linear-gradient(180deg, var(--figure-blue), #1d4464);
    border-radius: 60px 60px 10px 10px;
  }
  .company-name {
    position: absolute;
    left: 302px; top: 103px;
    margin: 0;
    font-size: 40px;
    font-weight: 400;
    color: var(--brand-blue-dark);
    white-space: nowrap;
  }
  .person-name {
    position: absolute;
    left: 407px; top: 207px;
    margin: 0;
    font-size: 36px;
    color: var(--paper);
    white-space: nowrap;
  }
  .contact {
    position: absolute;
    left: 536px;
    margin: 0;
    color: var(--brand-blue-dark);
    white-space: nowrap;
  }
  .contact-phone {
    top: 392px;
    font-family: "Tinos", "Times New Roman", serif;
    font-size: 21px;
  }
  .contact-email {
    top: 436px;
    font-family: "Tinos", "Times New Roman", serif;
    font-size: 18px;
  }
  .contact-email .address {
    font-family: "Arimo", Arial, sans-serif;
    font-weight: 700;
    font-size: 17px;
  }
  .website {
    position: absolute;
    left: 192px; top: 527px;
    margin: 0;
    font-size: 28px;
    white-space: nowrap;
    background: linear-gradient(90deg, var(--brand-blue-dark) 0 325px, var(--paper) 325px 100%);
    -webkit-background-clip: text;
    background-clip: text;
    color: transparent;
  }
</style>
</head>
<body>
  <div class="business-card">
    <div class="panel-left"></div>
    <div class="footer-strip-right"></div>
    <div class="title-band"></div>
    <div class="name-band"></div>
    <div class="pointing-hand-left" role="img" aria-label="Illustrated hand in a sleeve pointing left"></div>
    <div class="pointing-hand-right" role="img" aria-label="Illustrated hand in a sleeve pointing right"></div>
    <div class="consultant-figure" role="img" aria-label="Cartoon businessman in a blue suit giving a thumbs up and holding a briefcase"></div>

    <h1 class="company-name">The Patron Journey Mentor</h1>
    <p class="person-name">Martin Glenholme</p>
    <p class="contact contact-phone">P: +61 400 582316</p>
    <p class="contact contact-email">E: <span class="address">martin@ThePatronJourneyMentor.example</span></p>
    <p class="website">http://www.ThePatronJourneyMentor.example</p>
  </div>
</body>
</html>
```